Tallyspot.com.au Advertising Flyer.

www.tallyspot.com.au is an Australian discount voucher website with mobile capability. We provide free discount vouchers to consumers and affordable advertising to small to medium sized businesses.

We're about to launch a consumer based affiliate program, whereby our subscribers can earn gift cards by referring a business. When a consumer joins our program, we'll be sending them 50-100 promotional cards(a5) offering a 70% discount on advertising to entice local businesses to get on board.

More details on the program can be found here:
http://www.tallyspot.com.au/tallycrew.php

We require professional cards that drive home the value of promoting with tallyspot.com.au:

This particular promotion theme/heading is;

"Turn your spare change into customers with Tallyspot.com.au!"

* For a limited time you can promote your business to thousands of local customers already looking for deals.
* Over 50,000+ members and growing rapidly.
* Exclusive 70% Discount Code
* Guaranteed Results or your Money Back.
* Local, Targeted and Measurable - Advertising that works!

For additional reference on our advertising, our standard (long copy) sales page is:
http://www.tallyspot.com.au/advertising.php

Spec/Requirements:
- A5
- Double Sided
- Front = Main marketing copy
- Back = Graphic display of website features + business listing + mobile screenshot.
(End product will be printed on 200+gsm and no bleed.)

Feel free to use any of the messages/phrases listed above, and both sides should have room for approximately 100 words of additional copy and contact details/call to action.

We absolutely love creativity, and doing things a little bit differently. In saying that, we have recently rebranded to Tallyspot.com.au so the flyer should effectively represent the brand.

If you require any additional information or files, I am available at any time via ned@brimfulbasket.com.au - feel free to shoot me request for any images you require.

Target Market(s)

Australian small to medium business owners - retail, restaurants, cafes, shopping, travel, entertainment......

Industry/Entity Type

Advertising

Requirements
Must have
• - A5
• - Double Sided
• - Front = Main marketing copy
• - Back = Graphic display of website features + business listing + mobile screenshot.
• (End product will be printed on 200+gsm and no bleed.)
Nice to have
• Inclusion/incorporation of our pig mascot - but not compulsory.

```html
<!DOCTYPE html>
<html lang="en">
<head>
<meta charset="utf-8">
<title>Tallyspot.com.au Advertising Flyer</title>
<link rel="stylesheet" href="https://fonts.googleapis.com/css2?family=Didact+Gothic&family=Nunito:wght@400;700;800&display=swap">
<style>
:root{
  --paper:#f2efe8;
  --paper-edge:#e6e1d6;
  --ink:#4a4a4a;
  --kraft:#c8b48a;
  --kraft-dark:#a8936a;
  --green:#a3c13a;
  --green-dark:#7f9a22;
  --teal:#2aa3b9;
  --yellow:#f2bf1d;
  --pink:#e9689a;
  --red:#e0574b;
  --navy:#1e5b86;
  --white:#ffffff;
  --black:#111111;
  --mascot:#b4cf45;
}
*{box-sizing:border-box;margin:0;padding:0}
html,body{width:849px;height:1200px;overflow:hidden;background:var(--paper)}
body{font-family:"Didact Gothic",sans-serif;color:var(--ink)}
.flyer{position:relative;width:849px;height:1200px;overflow:hidden;
  background:linear-gradient(180deg,var(--paper) 0%,#f5f3ee 60%,var(--paper-edge) 100%)}
.abs{position:absolute}

/* faint mascot stamp */
.mascot-stamp{left:640px;top:10px;width:200px;height:160px;border-radius:50%;
  background:radial-gradient(circle,rgba(214,170,90,.28),rgba(214,170,90,0) 70%)}

/* website panel */
.site{left:40px;top:33px;width:587px;height:634px;background:var(--white);
  box-shadow:0 3px 10px rgba(0,0,0,.25)}
.site-head{left:18px;top:27px;width:569px;height:353px;background:var(--kraft)}
.site-nav{left:273px;top:40px;display:flex;gap:0;font-family:"Nunito",sans-serif;font-size:9px}
.site-nav span{background:var(--white);padding:3px 6px;border-right:1px solid #ddd}
.site-nav .login{background:var(--green);color:var(--white);font-weight:700;margin-left:8px;border:0;padding:3px 9px}
.brand-name{left:38px;top:85px;font-family:"Didact Gothic",sans-serif;font-size:27px;color:var(--navy)}
.brand-dot{left:42px;top:125px;width:14px;height:14px;border-radius:50%;background:var(--navy)}
.tagline{left:293px;top:60px;width:255px;height:74px;background:var(--red);transform:rotate(-3deg);
  color:var(--white);font-family:"Nunito",sans-serif;font-weight:800;font-size:24px;padding:10px 16px;line-height:1}
.search-box{left:47px;top:153px;width:260px;height:93px;background:var(--green);padding:12px 14px;color:var(--white)}
.search-box h2{font-family:"Nunito",sans-serif;font-size:19px;font-weight:800;margin-left:44px}
.search-row{display:flex;gap:6px;margin-top:18px}
.search-input{flex:1;background:var(--white);color:#888;font-size:10px;padding:4px 6px}
.search-btn{background:var(--white);color:var(--green-dark);font-size:10px;padding:4px 10px;border-radius:3px}
.search-icon{left:56px;top:160px}
.advanced{left:187px;top:268px;font-family:"Nunito",sans-serif;font-size:11px;font-weight:700;color:var(--green-dark)}
.cats{left:320px;top:164px;display:grid;grid-template-columns:90px 90px;row-gap:9px;column-gap:10px;
  font-family:"Nunito",sans-serif;font-size:12px;color:var(--white)}
.cats span::before{content:"";display:inline-block;width:8px;height:8px;background:var(--white);margin-right:6px;border-radius:2px;opacity:.8}
.steps-band{left:18px;top:292px;width:569px;height:82px;background:#f6f3ea}
.steps-title{left:24px;top:300px;font-family:"Nunito",sans-serif;font-weight:800;font-size:20px;line-height:1.05;color:var(--kraft-dark)}
.step{top:296px;height:74px;color:var(--white);padding:6px 8px;font-family:"Nunito",sans-serif}
.step b{font-size:30px;font-weight:800;line-height:1;margin-right:4px;float:left}
.step strong{font-size:15px;font-weight:800;display:block;line-height:1}
.step small{display:block;clear:both;font-size:7px;line-height:1.2;margin-top:4px}
.step-1{left:155px;width:138px;background:var(--teal)}
.step-2{left:300px;width:134px;background:var(--yellow)}
.step-3{left:441px;width:146px;background:var(--green)}
.social-box{left:37px;top:370px;width:123px;height:130px;border:1px solid #ddd;padding:6px;font-size:8px;font-family:"Nunito",sans-serif}
.social-box .name{font-weight:700;color:var(--navy);font-size:9px}
.avatars{display:flex;gap:5px;margin:6px 0}
.avatars i{display:block;width:26px;height:26px;background:#c9b7a6}
.side-cta{left:37px;width:123px;font-family:"Nunito",sans-serif;font-weight:800;font-size:11px;color:var(--red);display:flex;gap:6px;align-items:center}
.side-cta .ic{width:32px;height:40px;flex:none}
.side-cta.news{color:var(--green-dark)}
.featured{left:177px;top:373px;width:270px;height:26px;background:var(--pink);color:var(--white);
  font-family:"Nunito",sans-serif;font-weight:800;font-size:12px;padding:5px 14px}
.search-mini{left:470px;top:376px;font-size:10px;color:#666}
.coupon{top:407px;width:132px;height:213px;border:2px dashed #f0a6c1;padding:6px;font-family:"Nunito",sans-serif;font-size:8px}
.coupon h4{font-size:8px;font-weight:700;color:#555;border-bottom:1px solid #eee;padding-bottom:4px}
.coupon .deal{font-size:10px;font-weight:800;color:var(--red);margin:6px 0 4px;line-height:1.15}
.coupon .pic{height:62px;margin-bottom:6px}
.coupon .view{display:inline-block;background:var(--pink);color:var(--white);padding:2px 5px;margin-top:6px;font-size:7px}
.c1{left:177px}.c2{left:317px}.c3{left:456px}

/* phone */
.phone{left:553px;top:107px;width:280px;height:560px;border-radius:44px;background:var(--black);
  box-shadow:0 6px 18px rgba(0,0,0,.4);border:3px solid #9a9a9a}
.speaker{left:680px;top:165px;width:34px;height:5px;border-radius:3px;background:#444}
.screen{left:587px;top:207px;width:220px;height:316px;background:#e9e4da;overflow:hidden;font-family:"Nunito",sans-serif}
.status{height:14px;background:#1d1d1d;color:#ddd;font-size:8px;display:flex;justify-content:space-between;padding:1px 5px}
.urlbar{background:#b5bfcb;padding:3px 5px;font-size:7px}
.urlbar span{display:block;background:var(--white);border-radius:8px;padding:2px 6px;color:#444}
.tabs{display:flex;justify-content:space-around;background:#3d3d3d;color:#ddd;font-size:7px;padding:3px 0}
.m-head{background:var(--kraft);padding:8px 8px 10px}
.m-brand{font-size:14px;color:var(--navy);font-family:"Didact Gothic",sans-serif;margin-bottom:6px}
.m-form{background:#f4efe3;padding:6px;border-radius:3px;font-size:9px}
.m-form h5{font-size:12px;font-weight:800;color:#333;text-align:center}
.m-field{background:var(--white);border:1px solid #bbb;padding:2px 5px;margin-top:4px;font-weight:700}
.m-select{background:#eee;border:1px solid #bbb;padding:1px 5px;margin-top:4px;font-size:8px}
.m-btn{background:#ddd;border:1px solid #aaa;text-align:center;margin-top:4px;font-size:8px;border-radius:8px}
.m-row{display:flex;justify-content:space-between;margin-top:6px}
.m-row span{background:var(--white);border:1px solid #999;padding:2px 10px;font-size:8px;font-weight:700}
.m-foot{background:#cfcfcf;height:40px}
.home-btn{left:670px;top:564px;width:46px;height:46px;border-radius:50%;border:2px solid #444;background:#1a1a1a}

/* copy */
.features{top:710px;list-style:none;font-size:20px;line-height:24px;color:var(--ink)}
.features li::before{content:"•"}
.features-left{left:73px;top:712px}
.features-right{left:457px;top:709px}
.body-copy{left:73px;top:900px;width:714px;font-size:18.6px;line-height:28px;color:#3d3d3d}
.mascot{left:287px;top:1040px;width:150px;height:113px;border-radius:50%;
  background:radial-gradient(ellipse,rgba(180,207,69,.45),rgba(180,207,69,.12) 70%,rgba(180,207,69,0) 72%)}
.contact{left:456px;top:1053px;font-size:15.5px;line-height:21px;color:#555}
</style>
</head>
<body>
<main class="flyer">
  <div class="abs mascot-stamp" role="img" aria-label="Faint stamped pig mascot decoration"></div>

  <section class="abs site" aria-label="Website preview">
  </section>
  <div class="abs site-head"></div>
  <nav class="abs site-nav"><span>home</span><span>search</span><span>featured offers</span><span>advertising</span><span>help!</span><span>contact</span><span class="login">login</span></nav>
  <div class="abs brand-name">Tallyspot.com.au</div>
  <div class="abs tagline">savings made simple.</div>
  <div class="abs search-box">
    <h2>SEARCH for vouchers</h2>
    <div class="search-row"><span class="search-input">suburb, postcode</span><span class="search-btn">search</span></div>
  </div>
  <svg class="abs search-icon" width="38" height="38" viewBox="0 0 38 38" aria-hidden="true">
    <circle cx="15" cy="15" r="11" fill="none" stroke="#fff" stroke-width="3"/>
    <line x1="23" y1="23" x2="34" y2="34" stroke="#fff" stroke-width="4" stroke-linecap="round"/>
  </svg>
  <div class="abs cats"><span>Automotive</span><span>Entertainment</span><span>Financial</span><span>Food</span><span>Retail</span><span>Services</span></div>
  <div class="abs advanced">advanced search &gt;&gt;</div>

  <div class="abs steps-band"></div>
  <div class="abs steps-title">saving is<br>easier than<br>ever!</div>
  <div class="abs step step-1"><b>1</b><strong>search</strong><small>Simply type in a suburb or postcode.</small></div>
  <div class="abs step step-2"><b>2</b><strong>print or<br>mobile</strong><small>Print your voucher or show it on mobile.</small></div>
  <div class="abs step step-3"><b>3</b><strong>save!</strong><small>Start saving. It's that easy!</small></div>

  <div class="abs social-box">
    <div class="name">Brimful Basket</div>
    <div>You like this.</div>
    <div style="margin-top:8px">4,105 people like Brimful Basket</div>
    <div class="avatars" role="img" aria-label="Member profile photos"><i></i><i></i><i></i></div>
    <div>Ana &nbsp; Liv &nbsp; Mara</div>
  </div>
  <div class="abs side-cta" style="top:507px">
    <svg class="ic" viewBox="0 0 32 40" aria-hidden="true"><rect x="6" y="2" width="20" height="36" rx="4" fill="#e0574b"/><rect x="9" y="7" width="14" height="22" fill="#fff"/></svg>
    <span>Save with us on your mobile</span>
  </div>
  <div class="abs side-cta news" style="top:565px">
    <svg class="ic" viewBox="0 0 32 40" aria-hidden="true"><rect x="2" y="10" width="28" height="20" fill="#7f9a22"/><polyline points="2,10 16,22 30,10" fill="none" stroke="#fff" stroke-width="2"/></svg>
    <span>E-mail Newsletter signup!</span>
  </div>

  <div class="abs featured">Featured Listings</div>
  <div class="abs search-mini">search</div>
  <article class="abs coupon c1">
    <h4>Reel Stop New Farm</h4>
    <p class="deal">Rent 1 New Release Get THREE Weeklies FREE!</p>
    <div class="pic" role="img" aria-label="Video store offer artwork" style="background:linear-gradient(135deg,#f2bf1d,#2a2a2a)"></div>
    <p>Rent 1 new release, get three weeklies free.</p>
    <span class="view">view voucher</span>
  </article>
  <article class="abs coupon c2">
    <h4>Seller's store unavailable</h4>
    <p class="deal">4 x Quarter Chicken and Chips ONLY $15.95</p>
    <div class="pic" role="img" aria-label="Chicken and chips meal photo" style="background:linear-gradient(135deg,#e0574b,#f2bf1d)"></div>
    <p>Finals time means great eats from our friends.</p>
    <span class="view">view voucher</span>
  </article>
  <article class="abs coupon c3">
    <h4>Seller's store unavailable</h4>
    <p class="deal">FREE Examination</p>
    <div class="pic" role="img" aria-label="Optometrist offer artwork" style="background:linear-gradient(135deg,#2aa3b9,#ffffff)"></div>
    <p>Free exam with any new frame.</p>
    <span class="view">view voucher</span>
  </article>

  <div class="abs phone"></div>
  <div class="abs speaker"></div>
  <div class="abs screen">
    <div class="status"><span>Carrier</span><span>3:22 PM</span><span>▮</span></div>
    <div class="urlbar"><span>http://mobile.tallyspot.com.au/</span></div>
    <div class="tabs"><span>Search</span><span>Faves</span><span>Featured</span><span>Help/About</span></div>
    <div class="m-head">
      <div class="m-brand">Tallyspot.com.au</div>
      <div class="m-form">
        <h5>Enter your Postcode!</h5>
        <div class="m-field">Suburb, postcode</div>
        <div class="m-select">Select Category...</div>
        <div class="m-btn">Search</div>
        <div class="m-row"><span>Login</span><span>View Full Site</span></div>
      </div>
    </div>
    <div class="m-foot"></div>
  </div>
  <div class="abs home-btn"></div>

  <ul class="abs features features-left">
    <li>Discount vouchers</li>
    <li>voucher Marketing</li>
    <li>Australian Discount Codes</li>
    <li>Book Vouchers</li>
    <li>Free Pizza vouchers</li>
    <li>Computer Discount vouchers</li>
    <li>Beauty Treatment Vouchers</li>
  </ul>
  <ul class="abs features features-right">
    <li>Online Restaurant vouchers</li>
    <li>Discount Fuel Vouchers</li>
    <li>Car Wash vouchers</li>
    <li>Cinema Vouchers</li>
    <li>Gym Vouchers</li>
    <li>Car Rental vouchers</li>
    <li>Sports Vouchers</li>
  </ul>

  <p class="abs body-copy">100 words Lorem Ipsum is simply dummy text of the printing and typesetting industry. Lorem Ipsum has been the industry's standard dummy text ever since the 1500s, when an unknown printer took a galley of type and scrambled it to make a type specimen book. It has survived not only five centuries, but also the leap into electronic typesetting, remaining essentially unchanged.</p>

  <div class="abs mascot" role="img" aria-label="Green line drawing of the pig mascot"></div>
  <address class="abs contact" style="font-style:normal">
    PO Box 312 Coomera &nbsp;|&nbsp; QLD Australia 4209<br>
    ABN: 62418905337<br>
    Tel: (07) 5510 4472<br>
    Email: support@brimfulbasket.com.au
  </address>
</main>
</body>
</html>
```